Flyer to promote new Commercial HVAC Preventative Maintenance clients

This flyer will be in the body of emails that will be sent to new, existing, and/or potential commericial buildings HVAC clients. It will have the least amount of words used, but it will convey the point with pertinent pictorial and graphics. It will show the value of a Periodic/Preventative routine maintenance to lower operating costs of their commericial buildings (i.e. office, medical, shopping centers, apartment, warehouse facility, etc.), in the following ways:
1) Reduce monthly power usage,
2) Reduce emergency HVAC service calls,
3) Reduce costly repairs costs,
4) Reduce HVAC down-times and angry tenants,
5) Increases the life expectancy of the existing and/or new HVAC equipment in the building and/or the equipment's' early replacement costs,
6) Reduces tenant's early termination of their lease and law suits against the landlords,
7) Increases tenant's renewal of the lease and agree to pay the increase rental rates,
8) Reduces unhappy customers and increases tenant's productivity,
9) By reducing the landlord's expenses, the value of the property will increase considerably and profitable to sell their holdings, or refinance and keep their holdings with an increased ROI (Return On Investment).

Landlords can not depend on their tenants' obligation to maintain the landlords' major assets, which is their HVAC equipment and systems.

With the periodic maintenance done by one reliable and licensed HVAC company, the will not use different companies that may or may not do the right repair job on their unit and hurt their bottom line and increase HVAC replacement COSTLY rates.

```html
<!DOCTYPE html>
<html lang="en">
<head>
<meta charset="utf-8">
<title>Commercial HVAC Preventative Maintenance</title>
<link href="https://fonts.googleapis.com/css2?family=Bebas+Neue&family=Roboto+Condensed:wght@300;700&display=swap" rel="stylesheet">
<style>
  :root {
    --brand-blue: #2e6fbe;
    --heading-blue: #2a62b0;
    --accent-orange: #f08a2c;
    --body-grey: #55585c;
    --paper: #f6f7f9;
    --white: #ffffff;
  }
  * { margin: 0; padding: 0; box-sizing: border-box; }
  html, body { width: 779px; height: 1200px; overflow: hidden; background: var(--white); }
  .flyer {
    position: relative;
    width: 779px;
    height: 1200px;
    overflow: hidden;
    background: linear-gradient(180deg, #eef0f3 0%, var(--paper) 60%, #ffffff 100%);
    font-family: "Roboto Condensed", sans-serif;
  }
  .backdrop { position: absolute; inset: 0; width: 779px; height: 1200px; }
  .welcome {
    position: absolute;
    left: 57px; top: 50px; width: 280px;
    font-family: "Bebas Neue", sans-serif;
    font-size: 25.5px; line-height: 28.5px;
    color: var(--white);
    letter-spacing: 0.2px;
  }
  .welcome .highlight { color: var(--accent-orange); }
  .benefits-title {
    position: absolute;
    left: 415px; top: 600px;
    font-family: "Bebas Neue", sans-serif;
  }
  .benefits-title .lead { display: block; color: var(--accent-orange); font-size: 33px; line-height: 34px; }
  .benefits-title .main { display: block; color: var(--heading-blue); font-size: 44px; line-height: 44px; }
  .benefit-list {
    position: absolute;
    left: 355px; top: 700px; width: 392px;
    list-style: none;
    font-weight: 300;
    font-size: 13.6px; line-height: 21.6px;
    color: var(--body-grey);
  }
  .benefit-list li { position: relative; padding-left: 22px; }
  .benefit-list .num {
    position: absolute; left: 0; top: 2px;
    width: 17px; height: 17px;
    border: 1.3px solid var(--accent-orange);
    border-radius: 50%;
    font-size: 12px; line-height: 15px;
    text-align: center;
    color: var(--body-grey);
  }
  .one-company {
    position: absolute;
    left: 57px; top: 970px; width: 230px;
    font-weight: 700;
    font-size: 15px; line-height: 19.8px;
    color: var(--white);
  }
  .landlord-note {
    position: absolute;
    left: 415px; top: 1061px; width: 345px;
    font-weight: 700;
    font-size: 15.3px; line-height: 19.8px;
    color: var(--heading-blue);
  }
</style>
</head>
<body>
<main class="flyer">
  <svg class="backdrop" viewBox="0 0 1260 1942" preserveAspectRatio="none" aria-hidden="false">
    <defs>
      <linearGradient id="technicianTones" x1="0" y1="0" x2="1" y2="1">
        <stop offset="0" stop-color="#dfe5ec"/>
        <stop offset="0.45" stop-color="#a9c1dc"/>
        <stop offset="1" stop-color="#4f7fb8"/>
      </linearGradient>
      <linearGradient id="equipmentTones" x1="0" y1="0" x2="1" y2="1">
        <stop offset="0" stop-color="#cfd3d8"/>
        <stop offset="0.5" stop-color="#9ea4ab"/>
        <stop offset="1" stop-color="#6f757c"/>
      </linearGradient>
    </defs>
    <polygon class="brand-panel" points="0,0 632,0 395,1460 735,1942 0,1942" fill="var(--brand-blue)"/>
    <g role="img" aria-label="Smiling HVAC technician in a blue work shirt with arms crossed">
      <polygon points="632,0 1260,0 1260,980 535,855" fill="url(#technicianTones)"/>
    </g>
    <g role="img" aria-label="Industrial HVAC unit with silver ductwork and fan grille">
      <polygon points="40,470 608,495 400,1460 40,1390" fill="url(#equipmentTones)"/>
    </g>
  </svg>

  <p class="welcome">Whether you're an existing client or a potential partner, we appreciate the trust you've placed in us. To our new clients, we're excited to embark on a <span class="highlight">journey of excellence with you.</span></p>

  <h2 class="benefits-title">
    <span class="lead">Here's why we are your</span>
    <span class="main">Trusted HVAC Expert:</span>
  </h2>

  <ol class="benefit-list">
    <li><span class="num">1</span>Reduce monthly power usage.</li>
    <li><span class="num">2</span>Reduce emergency HVAC service calls.</li>
    <li><span class="num">3</span>Reduce costly repairs costs.</li>
    <li><span class="num">4</span>Reduce HVAC down-times and angry tenants.</li>
    <li><span class="num">5</span>Increases the life expectancy of the existing and/or new HVAC equipment in the building and/or the equipment's' early replacement costs.</li>
    <li><span class="num">6</span>Reduces tenant's early termination of their lease and law suits against the landlords.</li>
    <li><span class="num">7</span>Increases tenant's renewal of the lease and agree to pay the increase rental rates.</li>
    <li><span class="num">8</span>Reduces unhappy customers and increases tenant's productivity.</li>
    <li><span class="num">9</span>By reducing the landlord's expenses, the value of the property will increase considerably and profitable to sell their holdings, or refinance and keep their holdings with an increased ROI (Return On Investment).</li>
  </ol>

  <p class="one-company">With the periodic maintenance done by one reliable and licensed HVAC company, the will not use different companies that may or may not do the right repair job on their unit and hurt their bottom line and increase HVAC replacement COSTLY rates.</p>

  <p class="landlord-note">Landlords can not depend on their tenants' obligation to maintain the landlords' major assets, which is their HVAC equipment and systems.</p>
</main>
</body>
</html>
```